Business Card Design Project

Hi,

We are a new modern sheet metal business and I require a business card for our sales reps.

The card should be double sided and standout in a crowd.

I have attached our logo and our website is www.folvik.com.au.

Please ask if you have any further questions
Updates

hi everyone, 

I'm wondering if we can try to lighten the cards mood.  Everyone is using black and I'm not sure how that would be accepted in real life.

Gregory

Reason: Still No receiving what I was hoping for.

Industry/Entity Type

Business

Requirements
Must have
• double sided

```html
<!DOCTYPE html>
<html lang="en">
<head>
<meta charset="utf-8">
<title>Folvik Sheetmetal – Business Card</title>
<link rel="stylesheet" href="https://fonts.googleapis.com/css2?family=Montserrat:wght@600;700&family=Nunito+Sans:wght@400&family=Arimo:wght@400&display=swap">
<style>
  :root {
    --navy: #233a72;
    --white: #ffffff;
    --page: #ffffff;
    --steel: #5b5e63;
    --shadow: rgba(0, 0, 0, 0.18);
  }
  * { box-sizing: border-box; margin: 0; padding: 0; }
  html, body {
    width: 980px;
    height: 1200px;
    overflow: hidden;
    background: var(--page);
  }
  .canvas {
    position: relative;
    width: 980px;
    height: 1200px;
  }
  .card {
    position: absolute;
    left: 153px;
    width: 684px;
    height: 390px;
    box-shadow: 3px 4px 10px var(--shadow);
  }
  .card--front { top: 150px; background: var(--white); }
  .card--back { top: 673px; background: var(--navy); }

  /* Front */
  .brand {
    position: absolute;
    left: 0;
    right: 0;
    top: 128px;
    display: flex;
    justify-content: center;
    align-items: center;
    gap: 18px;
  }
  .brand__mark {
    width: 54px;
    height: 54px;
    background: var(--navy);
  }
  .brand__name {
    font-family: "Montserrat", sans-serif;
    font-weight: 700;
    font-size: 44px;
    letter-spacing: 2px;
    color: var(--navy);
  }
  .tagline {
    position: absolute;
    left: 0;
    right: 0;
    top: 292px;
    text-align: center;
    font-family: "Nunito Sans", sans-serif;
    font-size: 19px;
    color: var(--steel);
  }
  .tagline__divider {
    display: inline-block;
    width: 3px;
    height: 20px;
    margin: 0 8px;
    background: var(--navy);
    vertical-align: -4px;
  }

  /* Back */
  .name-band {
    position: absolute;
    left: 72px;
    top: 69px;
    width: 543px;
    height: 78px;
    background: var(--white);
    padding: 8px 0 0 12px;
    color: var(--navy);
    font-family: "Montserrat", sans-serif;
  }
  .name-band__name {
    font-size: 28px;
    font-weight: 700;
    letter-spacing: 2px;
    line-height: 34px;
  }
  .name-band__role {
    font-size: 24px;
    font-weight: 600;
    line-height: 30px;
  }
  .contact {
    position: absolute;
    top: 262px;
    font-family: "Arimo", sans-serif;
    font-size: 16px;
    line-height: 20px;
    color: var(--white);
  }
  .contact--address { left: 87px; }
  .contact--direct { left: 411px; }
  .contact__label { display: inline-block; width: 20px; }
</style>
</head>
<body>
<main class="canvas">
  <section class="card card--front" aria-label="Card front">
    <div class="brand">
      <span class="brand__mark"></span>
      <span class="brand__name">FOLVIK SHEETMETAL</span>
    </div>
    <p class="tagline">Flashings<span class="tagline__divider"></span>Gutter<span class="tagline__divider"></span>Rainwater Goods</p>
  </section>

  <section class="card card--back" aria-label="Card back">
    <div class="name-band">
      <p class="name-band__name">DANIEL HARLOW</p>
      <p class="name-band__role">Sales Representative</p>
    </div>
    <address class="contact contact--address" style="font-style:normal">
      22 Quarry Road Ridgeview Q 4301<br>
      PO Box 318 Ridgeview Q 4301<br>
      www.folvik.com.au
    </address>
    <address class="contact contact--direct" style="font-style:normal">
      <span class="contact__label">T</span>3904 5512<br>
      <span class="contact__label">F</span>3904 5513<br>
      email@folvik.com.au
    </address>
  </section>
</main>
</body>
</html>
```